Banner Ad for Weight Loss Product Site

We need a banner ad design for a new company selling a weight loss online programme (Ebook). The product is called "Slim Quill" and is suitable for people that want to lose weight fast and without doing sports, regardless of age. We would like to see designs that are eye-catching and at its best animated like in the example files. The final design should exhibit a professional look that encourages the customers to buy our product. The text should be "Persönlicher Diätplan zum Abnehmen?" as a title and "Jetzt informieren" for the button field. Thank you!

```html
<!DOCTYPE html>
<html lang="de">
<head>
<meta charset="utf-8">
<title>Slim Quill – Banner Set</title>
<link rel="stylesheet" href="https://fonts.googleapis.com/css2?family=Roboto+Condensed:wght@700&family=Ubuntu:wght@700&display=swap">
<style>
  :root{
    --page-bg:#ececec;
    --caption:#6f6f6f;
    --green:#3f9c12;
    --gold:#f3c61c;
    --orange-top:#ffc02a;
    --orange-bottom:#f27a00;
    --button-text:#2d1a05;
    --white:#ffffff;
    --panel-grey:#eeeeee;
  }
  *{margin:0;padding:0;box-sizing:border-box}
  html,body{width:1200px;height:841px;overflow:hidden}
  body{
    background:radial-gradient(circle at 50% 40%,#f4f4f4 0%,var(--page-bg) 70%);
    position:relative;
    font-family:"Roboto Condensed",Arial,sans-serif;
  }
  .caption{
    position:absolute;left:0;width:1200px;text-align:center;
    font-family:"Ubuntu",Arial,sans-serif;font-weight:700;
    color:var(--caption);font-size:37px;letter-spacing:1px;line-height:44px;
  }
  .caption--top{top:33px}
  .caption--bottom{top:706px}

  .banner{position:absolute;overflow:hidden;background:linear-gradient(180deg,var(--white),var(--panel-grey));}
  .banner__bg{position:absolute;inset:0;width:100%;height:100%}
  .brand{position:absolute;font-weight:700;line-height:1.05;text-align:center}
  .headline{position:absolute;color:var(--green);font-weight:700;line-height:1.12}
  .photo{position:absolute;background:linear-gradient(160deg,#e9d9c8 0%,#c99b7c 45%,#e4ecd6 80%);border-radius:4px}
  .cta{
    position:absolute;display:flex;align-items:center;justify-content:center;gap:8px;
    border-radius:999px;white-space:nowrap;
    background:linear-gradient(180deg,var(--orange-top),var(--orange-bottom));
    color:var(--button-text);font-weight:700;text-transform:uppercase;
    box-shadow:0 2px 3px rgba(0,0,0,.3);
  }
  .cta__arrow{display:block}

  /* Skyscraper */
  .banner--sky{left:76px;top:112px;width:320px;height:532px}
  .banner--sky .brand{left:0;width:320px;top:92px;font-size:36px;color:var(--green)}
  .banner--sky .headline{left:0;width:320px;top:160px;text-align:center;font-size:31px}
  .banner--sky .photo{left:22px;top:238px;width:280px;height:200px}
  .banner--sky .cta{left:29px;top:470px;width:263px;height:43px;font-size:21px}

  /* Leaderboard */
  .banner--wide{left:410px;top:112px;width:714px;height:184px}
  .banner--wide .brand{left:10px;width:124px;top:64px;font-size:30px;color:var(--green)}
  .banner--wide .headline{left:154px;top:20px;font-size:27px}
  .banner--wide .photo{left:312px;top:0;width:372px;height:184px;border-radius:0}
  .banner--wide .cta{left:154px;top:133px;width:148px;height:25px;font-size:12px}

  /* Small banner */
  .banner--small{left:410px;top:310px;width:458px;height:72px}
  .banner--small .brand{left:4px;width:66px;top:19px;font-size:16px;color:var(--white)}
  .banner--small .headline{left:91px;top:6px;font-size:14.5px;line-height:1.18}
  .banner--small .photo{left:219px;top:0;width:86px;height:72px;border-radius:0}
  .banner--small .cta{left:312px;top:23px;width:142px;height:24px;font-size:11.5px}

  .pointer{position:absolute}
</style>
</head>
<body>
  <p class="caption caption--top">IMAGES ARE SIZED DOWN FOR PREVIEW</p>

  <!-- Skyscraper 320 x 532 -->
  <section class="banner banner--sky">
    <svg class="banner__bg" viewBox="0 0 320 532" preserveAspectRatio="none" aria-hidden="true">
      <defs>
        <linearGradient id="skyGreen" x1="0" y1="0" x2="0" y2="1">
          <stop offset="0" stop-color="#b5e22a"/><stop offset="1" stop-color="#4f9d0e"/>
        </linearGradient>
      </defs>
      <path d="M0 0H320V58C240 40 120 50 0 70Z" fill="url(#skyGreen)"/>
      <path d="M0 70C120 50 240 40 320 58V66C240 50 120 60 0 80Z" fill="#f3c61c"/>
      <path d="M0 452C90 440 220 438 320 446V532H0Z" fill="url(#skyGreen)"/>
      <path d="M0 452C90 440 220 438 320 446V442C220 434 90 436 0 446Z" fill="#f3c61c"/>
    </svg>
    <div class="brand">Slim Quill</div>
    <h2 class="headline">Persönlicher Diätplan<br>zum Abnehmen?</h2>
    <div class="photo" role="img" aria-label="Smiling woman measuring her waist with a tape, beside the diet plan book and disc"></div>
    <svg class="pointer" style="left:36px;top:244px" width="16" height="24" viewBox="0 0 16 24" aria-hidden="true">
      <path d="M1 1V19L5.5 15L9 23L12 21.5L8.5 14H14Z" fill="#fff" stroke="#333" stroke-width="1.3"/>
    </svg>
    <div class="cta">Jetzt informieren
      <svg class="cta__arrow" width="12" height="14" viewBox="0 0 12 14" aria-hidden="true"><path d="M3 2L9 7L3 12" fill="none" stroke="#2d1a05" stroke-width="2.5"/></svg>
    </div>
  </section>

  <!-- Leaderboard 714 x 184 -->
  <section class="banner banner--wide">
    <svg class="banner__bg" viewBox="0 0 714 184" preserveAspectRatio="none" aria-hidden="true">
      <defs>
        <linearGradient id="wideGreen" x1="0" y1="0" x2="1" y2="1">
          <stop offset="0" stop-color="#b5e22a"/><stop offset="1" stop-color="#4f9d0e"/>
        </linearGradient>
      </defs>
      <path d="M0 0H120C70 8 25 28 0 60Z" fill="url(#wideGreen)"/>
      <path d="M0 60C25 28 70 8 120 0H130C75 10 28 32 0 68Z" fill="#f3c61c"/>
      <path d="M714 184H560C640 170 690 130 714 60Z" fill="url(#wideGreen)"/>
      <path d="M714 60C690 130 640 170 560 184H548C635 168 685 125 714 48Z" fill="#f3c61c"/>
    </svg>
    <div class="brand">Slim<br>Quill</div>
    <h2 class="headline">Persönlicher<br>Diätplan zum<br>Abnehmen?</h2>
    <div class="photo" role="img" aria-label="Smiling woman with measuring tape next to the diet plan book, disc and open pages"></div>
    <svg class="pointer" style="left:644px;top:28px" width="12" height="18" viewBox="0 0 16 24" aria-hidden="true">
      <path d="M1 1V19L5.5 15L9 23L12 21.5L8.5 14H14Z" fill="#fff" stroke="#333" stroke-width="1.3"/>
    </svg>
    <div class="cta">Jetzt informieren
      <svg class="cta__arrow" width="8" height="10" viewBox="0 0 12 14" aria-hidden="true"><path d="M3 2L9 7L3 12" fill="none" stroke="#2d1a05" stroke-width="2.5"/></svg>
    </div>
  </section>

  <!-- Small banner 458 x 72 -->
  <section class="banner banner--small">
    <svg class="banner__bg" viewBox="0 0 458 72" preserveAspectRatio="none" aria-hidden="true">
      <defs>
        <linearGradient id="smallGreen" x1="0" y1="0" x2="1" y2="0">
          <stop offset="0" stop-color="#8cc81c"/><stop offset="1" stop-color="#a9dc22"/>
        </linearGradient>
      </defs>
      <path d="M0 0H78C70 25 70 50 78 72H0Z" fill="url(#smallGreen)"/>
      <path d="M78 0C70 25 70 50 78 72H82C74 50 74 25 82 0Z" fill="#f3c61c"/>
      <path d="M458 0H300C310 25 310 50 300 72H458Z" fill="url(#smallGreen)"/>
      <path d="M300 0C310 25 310 50 300 72H296C306 50 306 25 296 0Z" fill="#f3c61c"/>
    </svg>
    <div class="brand">Slim<br>Quill</div>
    <h2 class="headline">Persönlicher<br>Diätplan zum<br>Abnehmen?</h2>
    <div class="photo" role="img" aria-label="Smiling woman measuring her waist"></div>
    <div class="cta">Jetzt informieren
      <svg class="cta__arrow" width="8" height="10" viewBox="0 0 12 14" aria-hidden="true"><path d="M3 2L9 7L3 12" fill="none" stroke="#2d1a05" stroke-width="2.5"/></svg>
    </div>
  </section>

  <p class="caption caption--bottom">CHECK THE LINKS IN THE DESCRIPTION<br>TO SEE THE ANIMATIONS</p>
</body>
</html>
```